world's hottest chilli salt 7 flavours

I am needing a packaging design for 7 different ones to reflect our range

We are located in Perth OZ. Our chilli salts are new and unique and the world’s hottest ones as we use the world’s hottest chillies. Our product is made from chilli and salts but then other flavours to make them different - one for example is a Smokey one which is very popular and it made from salt, chilli, chipotle, coriander, yellow mustard seeds and garlic.

the colour distinguishes the difference between the different flavours

ingredient list is on the website for each flavour
please view fierymolarz.com at our range of chilli salts

Target Market(s)

Male adults age is from 18 + - target market is Australian market but will be selling overseas as well to the US.

Industry/Entity Type

Product

Requirements
Must have
• must be colour code as examples i have uploaded whether or to view fierymolarsz.com -it it bigger or small i'm not fussed but there needs to be a distinction between the 7 different flavours. Size of label is 95mm x 37mm to work from so very small. The favour the heat (attached) needs to be somewhere on the logo but i would like to see what someone can do with that.
the logo is found with the tongue attached - this is needed and to be quite big if possible – we need the chilli image. It needs to be a good design where our customers and us go WOW.

text of the salts is found on the website.

barcode is needed along the right side. but do not include in the image i will put that on myself

also ingredient list - this is currently not looking any good.

needs to be the "worlds hottest" somewhere
Nice to have
• something clean crisp and elegant like

http://wrapgallerynook.example.com/2009/10/that-bottle.html

** this is what we would like http://img.pixhoardly.example.com/_9KqWmTzR2LP/XbNa-7QsdHo/ZZZZZZZZKL2/pTe4RRvWYCA/s1600/QLMX+tiles.jpg
clean crisp and
Should not have
• too many fonts

```html
<!DOCTYPE html>
<html lang="en">
<head>
<meta charset="utf-8">
<title>Mild Jalapeños Chilli Salt Label</title>
<link rel="stylesheet" href="https://fonts.googleapis.com/css2?family=Arimo:wght@400;700&display=swap">
<style>
  :root {
    --page: #ffffff;
    --label-bg: #2a2929;
    --ghost: #373536;
    --band: #00aeef;
    --blue-text: #27b4ea;
    --green: #8dc63f;
    --white: #ffffff;
    --grey-text: #e6e6e6;
    --mascot-light: #e8412f;
    --mascot-dark: #a9161c;
  }
  html, body {
    margin: 0;
    width: 1200px;
    height: 900px;
    overflow: hidden;
    background: var(--page);
    font-family: "Arimo", Arial, sans-serif;
  }
  .label {
    position: absolute;
    left: 25px;
    top: 226px;
    width: 1123px;
    height: 437px;
    background: var(--label-bg);
    overflow: hidden;
  }
  .ghost-word {
    position: absolute;
    left: 0;
    top: 0;
  }
  .band {
    position: absolute;
    background: var(--band);
    top: 113px;
    height: 100px;
  }
  .band--left { left: 0; width: 36px; }
  .band--right { left: 505px; right: 0; }
  .flavour-name {
    position: absolute;
    left: 58px;
    top: 33px;
    margin: 0;
    font-size: 37px;
    font-weight: 700;
    color: var(--green);
    white-space: nowrap;
  }
  .product-line {
    position: absolute;
    left: 54px;
    top: 107px;
    margin: 0;
    font-size: 33px;
    line-height: 37.5px;
    font-weight: 700;
    color: var(--blue-text);
    white-space: nowrap;
  }
  .description {
    position: absolute;
    left: 57px;
    top: 237px;
    margin: 0;
    font-size: 20.3px;
    line-height: 26px;
    color: var(--grey-text);
    white-space: nowrap;
  }
  .heat-rating {
    position: absolute;
    left: 55px;
    top: 348px;
    display: flex;
    align-items: center;
    height: 54px;
  }
  .heat-icon { width: 30px; height: 54px; }
  .heat-word {
    margin-left: 15px;
    font-size: 27px;
    color: var(--white);
  }
  .divider {
    width: 2px;
    height: 54px;
    background: var(--white);
    margin: 0 17px 0 16px;
  }
  .web {
    font-size: 25.5px;
    font-weight: 700;
    color: var(--white);
    white-space: nowrap;
  }
  .brand-mark {
    position: absolute;
    left: 928px;
    top: 22px;
    width: 146px;
    height: 242px;
  }
  .brand-art {
    position: absolute;
    left: 18px;
    top: 0;
    width: 110px;
    height: 242px;
    border-radius: 55px 55px 45px 45px;
    background: linear-gradient(165deg, var(--mascot-light), var(--mascot-dark));
  }
  .brand-name {
    position: absolute;
    left: 0;
    top: 188px;
    width: 146px;
    text-align: center;
    font-size: 25px;
    font-weight: 700;
    color: var(--white);
  }
  .maker {
    position: absolute;
    left: 948px;
    top: 289px;
    margin: 0;
    font-size: 16.5px;
    line-height: 18px;
    color: var(--grey-text);
  }
  .maker-origin { color: var(--green); display: block; }
  .net-weight {
    position: absolute;
    left: 947px;
    top: 364px;
    margin: 0;
    font-size: 28px;
    font-weight: 700;
    color: var(--green);
  }
</style>
</head>
<body>
<main class="label">
  <svg class="ghost-word" width="1123" height="437" viewBox="0 0 1123 437" aria-hidden="true">
    <g font-family="Arimo, Arial, sans-serif" font-weight="700" font-size="720" fill="var(--ghost)">
      <text transform="translate(-12 500) scale(0.62 1)">S</text>
      <text transform="translate(290 625) scale(0.62 1)">A</text>
      <text transform="translate(630 354) scale(0.62 1)">L</text>
      <text transform="translate(880 555) scale(0.62 1)">T</text>
    </g>
  </svg>

  <div class="band band--left"></div>
  <div class="band band--right"></div>

  <h1 class="flavour-name">MILD JALAPEÑOS</h1>
  <p class="product-line">Jalapeño Chilli<br>&amp; Pink Himilayan Rock Salt<br>Mixed with Herbs &amp; Spices</p>
  <p class="description">A mild chilli salt that can be used during cooking<br>or at the table for that extra something.</p>

  <div class="heat-rating">
    <svg class="heat-icon" viewBox="0 0 30 54" role="img" aria-label="Green chilli heat icon">
      <path d="M12 2 C14 6 16 8 18 10 C27 14 29 26 26 38 C23 49 12 54 4 50 C14 46 16 36 12 26 C9 18 8 12 12 10 C11 7 11 4 12 2 Z" fill="var(--green)"/>
    </svg>
    <span class="heat-word">MILD</span>
    <span class="divider"></span>
    <span class="web">fierymolarsz.com</span>
  </div>

  <div class="brand-mark">
    <div class="brand-art" role="img" aria-label="Chilli mascot illustration with flame"></div>
    <div class="brand-name">Ember Grin</div>
  </div>

  <p class="maker"><span class="maker-origin">MADE IN WA</span>PO BOX 742<br>Tarrowdale 6981</p>
  <p class="net-weight">100g</p>
</main>
</body>
</html>
```